Information flyer for 5 day treatment flyer

I am wanting a double sided flyer for my next 5 day treatment program for addictions. I have included the copy for the flyer as an attachment.
I have also included a drop box link to my brand guidelines and my logos. The logo I prefer is the grey horse with the words Willowmere Collective under.
https://www.filecrate.example/sh/k2jtq7wn3xb5lp1/BBQr9TzLm4Kd7c8NpWvY2hsXe?dl=0

https://www.filecrate.example/s/qm8vz2kt6bw9rc4/WILLOWMERE%20COLLECTIVE%20%7C%20Brand%20Identity%20Guidelines.pdf?dl=0
I have also included a copy of an existing flyer which I like very much and a documant with the copy.
https://www.filecrate.example/sh/t7wbn3kx9zq1mv5/CCRt2pLw8-nZ4Kj7FyTuGHs_b?dl=0

I prefer simple, elegant designs please. The design needs to show my clients that I know what I am doing and I am trust worthy and a skilled professional.

Here is the drop box link to the images I have selected for this program. The tones in the images I have selected are orange/red. Please feel free to pick what you think works well.
https://www.filecrate.example/sh/mrq5jv82lnc0tfw/DDDhW392Bx6Lp88_Q7KcZnRye?dl=0

Many thanks
Marisol

```html
<!DOCTYPE html>
<html lang="en">
<head>
<meta charset="utf-8">
<title>Behind Closed Doors — 5 Day Intensive Treatment Program</title>
<link rel="stylesheet" href="https://fonts.googleapis.com/css2?family=Montserrat:wght@400;600;900&display=swap">
<style>
  :root {
    --panel-top: rgba(24, 24, 36, 0.97);
    --panel-bottom: rgba(44, 46, 64, 0.96);
    --brand-grey: #d9d6cf;
    --title-violet: #7473a3;
    --text-white: #ffffff;
    --sky-warm: #f6c86a;
    --sky-red: #c8644f;
    --sky-blue: #6a7a8e;
    --room-dark: #2b2b35;
    --floor-light: #ece7dc;
  }
  * { box-sizing: border-box; margin: 0; padding: 0; }
  html, body {
    width: 902px;
    height: 1200px;
    overflow: hidden;
    background: #ffffff;
    font-family: "Montserrat", sans-serif;
  }
  .flyer-cover {
    position: relative;
    width: 902px;
    height: 1200px;
    overflow: hidden;
  }
  .cover-photo {
    position: absolute;
    inset: 0;
    background:
      radial-gradient(ellipse 180px 140px at 700px 670px, rgba(255, 250, 220, 0.95), rgba(255, 220, 120, 0) 100%),
      linear-gradient(to bottom, transparent 0, transparent 720px, var(--floor-light) 780px, #f7f4ee 1200px),
      linear-gradient(to bottom, var(--sky-blue) 140px, var(--sky-red) 330px, #b08a7a 470px, var(--sky-warm) 640px, #f3d9a0 740px),
      var(--room-dark);
  }
  .cover-photo::before {
    content: "";
    position: absolute;
    left: 0; top: 0;
    width: 510px; height: 1200px;
    background: var(--room-dark);
  }
  .cover-photo::after {
    content: "";
    position: absolute;
    left: 500px; top: 0;
    width: 402px; height: 150px;
    background: linear-gradient(to bottom, #5a6070, #e9ecef 120px, #ffffff 150px);
  }
  .content-panel {
    position: absolute;
    left: 0; top: 0;
    width: 498px;
    height: 1200px;
    border-radius: 0 50px 50px 0;
    background: linear-gradient(to bottom, var(--panel-top), var(--panel-bottom));
  }
  .brand-lockup {
    position: absolute;
    left: 0; top: 62px;
    width: 498px;
    text-align: center;
  }
  .brand-mark {
    width: 100px; height: 100px;
    margin: 0 auto 36px;
    border-radius: 50%;
    background: var(--brand-grey);
  }
  .brand-name {
    color: var(--brand-grey);
    font-weight: 400;
    font-size: 19px;
    line-height: 24px;
    letter-spacing: 3.5px;
  }
  .program-label {
    position: absolute;
    left: 39px; top: 813px;
    color: var(--text-white);
    font-weight: 600;
    font-size: 33px;
    line-height: 37px;
    white-space: nowrap;
  }
  .program-title {
    position: absolute;
    left: 38px; top: 894px;
    color: var(--title-violet);
    font-weight: 900;
    font-size: 88px;
    line-height: 80px;
    letter-spacing: -1px;
    white-space: nowrap;
  }
</style>
</head>
<body>
  <main class="flyer-cover">
    <div class="cover-photo" role="img" aria-label="Dim panelled room with white double doors open onto a glowing orange sunset sky above a pale wooden floor"></div>
    <section class="content-panel">
      <div class="brand-lockup">
        <div class="brand-mark"></div>
        <p class="brand-name">WILLOWMERE COLLECTIVE</p>
      </div>
      <p class="program-label">5 DAY INTENSIVE<br>TREATMENT PROGRAM</p>
      <h1 class="program-title">BEHIND<br>CLOSED<br>DOORS</h1>
    </section>
  </main>
</body>
</html>
```